Ridgeline Build Network Inc. Letterhead

Creation of attractive and eye catching letterhead for a business start-up for the construction industry. Letterhead must relate to construction, but avoid standard hammer and tools in the design.
Updates

I forgot to add some details, sorry about that. Some pertinent info: Ph: 541-555-0148 ridgelinebuildnet.example 487 Willowmere Ave, Ste 210 Larkhaven, OR 95699 info@ridgelinebuildnet.example not sure if slogan should be in there" “Connecting construction professionals to create a purpose driven industry.” must be able to be used in word. Thanks!

```html
<!DOCTYPE html>
<html lang="en">
<head>
<meta charset="utf-8">
<title>Ridgeline Build Network Inc. Letterhead</title>
<link rel="stylesheet" href="https://fonts.googleapis.com/css2?family=Roboto:wght@400;500;700&display=swap">
<style>
  :root {
    --brand-red: #b01c22;
    --brand-navy: #1d2353;
    --ink: #6a6a6a;
    --ink-dark: #555555;
    --rule-grey: #c4c4c4;
    --paper: #f3f3f3;
    --backdrop: #d6d6d6;
  }
  * { box-sizing: border-box; margin: 0; padding: 0; }
  html, body { width: 1200px; height: 1154px; overflow: hidden; }
  body {
    background: var(--backdrop);
    font-family: "Roboto", Arial, sans-serif;
    color: var(--ink);
    position: relative;
  }
  .letterhead {
    position: absolute;
    left: 211px; top: 27px;
    width: 778px; height: 1100px;
    background: var(--paper);
    overflow: hidden;
  }
  .brand {
    position: absolute;
    left: 69px; top: 118px;
    display: flex; align-items: center; gap: 10px;
  }
  .brand-mark { width: 14px; height: 14px; background: var(--brand-red); flex: none; }
  .brand-name {
    font-weight: 700; font-size: 20px; color: var(--brand-navy);
    line-height: 1.15; width: 190px;
  }
  .contact {
    position: absolute; left: 523px; top: 127px;
    font-style: normal;
    font-size: 12.5px; line-height: 19px; color: var(--ink-dark);
  }
  .contact-item { display: flex; align-items: center; gap: 7px; margin-top: 4px; }
  .contact-item.first { margin-top: 10px; }
  .contact-icon { width: 14px; height: 14px; flex: none; }
  .header-rule {
    position: absolute; left: 69px; top: 250px; width: 645px; height: 4px;
  }
  .header-rule .accent { position: absolute; left: 0; top: 0; width: 208px; height: 4px; background: var(--brand-red); }
  .header-rule .line { position: absolute; left: 208px; top: 2px; right: 0; height: 1px; background: var(--rule-grey); }
  .recipient {
    position: absolute; left: 69px; top: 385px;
    font-size: 13.5px; line-height: 20.5px;
  }
  .letter-body {
    position: absolute; left: 69px; top: 507px; width: 645px;
    font-size: 13.5px; line-height: 20.4px; text-align: justify;
  }
  .letter-body p + p { margin-top: 23px; }
  .signature {
    position: absolute; left: 67px; top: 812px; width: 148px; height: 82px;
    background: linear-gradient(135deg, rgba(176,28,34,0.14), rgba(176,28,34,0.04));
  }
  .signer-title {
    position: absolute; left: 67px; top: 916px; font-size: 13px;
  }
  .footer-rule {
    position: absolute; left: 0; right: 0; bottom: 44px; height: 3px;
    background: var(--brand-navy);
  }
  .footer-band {
    position: absolute; left: 0; right: 0; bottom: 0; height: 38px;
    background: var(--brand-red);
  }
  .footer-url {
    position: absolute; right: 60px; bottom: 11px;
    font-size: 13.5px; color: #fff;
  }
</style>
</head>
<body>
  <main class="letterhead">
    <div class="brand">
      <span class="brand-mark"></span>
      <span class="brand-name">Ridgeline Build Network Inc.</span>
    </div>

    <address class="contact">
      <div>487 Willowmere Ave</div>
      <div>Ste 210 Larkhaven, OR 95699</div>
      <div class="contact-item first">
        <svg class="contact-icon" viewBox="0 0 14 14" aria-hidden="true"><circle cx="7" cy="7" r="7" fill="#b01c22"/><path d="M4.3 3.6l1.6-.3.8 1.9-1 .7c.5 1.1 1.3 1.9 2.4 2.4l.7-1 1.9.8-.3 1.6c-3.4.1-6.2-2.7-6.1-6.1z" fill="#fff"/></svg>
        <span>541-555-0148</span>
      </div>
      <div class="contact-item">
        <svg class="contact-icon" viewBox="0 0 14 14" aria-hidden="true"><circle cx="7" cy="7" r="7" fill="#b01c22"/><rect x="3.5" y="4.5" width="7" height="5" fill="none" stroke="#fff" stroke-width="1"/><path d="M3.5 4.5L7 7.3l3.5-2.8" fill="none" stroke="#fff" stroke-width="1"/></svg>
        <span>info@ridgelinebuildnet.example</span>
      </div>
    </address>

    <div class="header-rule"><span class="accent"></span><span class="line"></span></div>

    <div class="recipient">
      <div>Dear Halvorsen</div>
      <div>Corvel Print Studio Corporation</div>
      <div>Department Design</div>
    </div>

    <section class="letter-body">
      <p>Lorem ipsum dolor sit amet, consectetuer adipiscing elit. Aenean commodo ligula eget dolor. Aenean massa. Cum sociis natoque penatibus et magnis dis parturient montes, nascetur ridiculus mus. Donec quam felis, ultricies nec, pellentesque eu, pretium quis, sem. Nulla consequat massa quis enim. Donec pede justo, fringilla vel, aliquet nec, vulputate eget, arcu. In enim justo, rhoncus ut, imperdiet a, venenatis vitae, justo. Nullam dictum felis eu pede mollis pretium. Integer tincidunt. Cras dapibus. Vivamus elementum semper nisi.Nullam dictum felis eu pede mollis pretium. Integer tincidunt. Cras dapibus. Vivamus elementum semper nisi.felis eu pede mollis pretium. Integer tincidunt. Cras dapibus.</p>
      <p>Quisque rutrum. Aenean imperdiet. Etiam ultricies nisi vel augue. Curabitur ullamcorper ultricies nisi. Nam eget dui. Etiam rhoncus. Maecenas tempus, tellus eget condimentum rhoncus, sem quam semper libero, sit amet adipiscing sem neque sed ipsum.felis pede mollis pretium. I am tincidunt. Cras dapibus.</p>
    </section>

    <div class="signature" role="img" aria-label="Handwritten signature of the director in red ink"></div>
    <div class="signer-title">Director/Excecutive Director</div>

    <div class="footer-rule"></div>
    <div class="footer-band"></div>
    <div class="footer-url">www.ridgelinebuildnet.example</div>
  </main>
</body>
</html>
```